Book Cover Design Project

I need a book cover for a book that we will be releasing in the next few months.

It is a business book aimed at small businesses and people who want to escape the 9 - 5 and start their own business.

We want it to look similar to: http://www.dalvonquisttv.example/wp-content/uploads/2010/03/snap-on.jpg and also the book designs that I have uploaded images for.

I quite like the grey / charcoal background and the bright lime green colours from the Copper Lantern logo that I have attached. However, anything bright would be good - I am prepared to be flexible with colours. The books I have attached are a high impact as well - being bright blue with white black font with a really cool font.

The book is titled:

The Quick Lane Venture

By Owen Tarsley

Still thinking of the tagline, for now just use "Start an Online Business in no time at all"

Room for a quote/testimonial on the front of the book at the bottom, and as well on the back.

For the back cover text just use dummy text and my photo that is attached for now as well.

Barcode ISBN on the back at the bottom - price will be $19.95

Needs to be in PSD so we can change the text from our end.

I really want to get a good template made that I can edit the text for as we are still developing the book, but I want to get the book cover done so I can start advertising that it will be arriving soon.

There will probably be alterations that I need help with later down the track so looking to work with someone closely on this, and I will pay you for any extra time down the track..

Sizes will probably be around: I think 20.5cm tall and 14cm wide would be good..

Not sure how thick for the spine, it will depend on how many words get cut off, but as an estimate probably 1.5CM..

Just added some more detail to the brief.. Please read it carefully.

Target Market(s)

small business owners, professionals who want to start their own business, soon to be entrepreneurs, entrepreneurs

Industry/Entity Type

Advertising

Requirements
Must have
• The Quick Lane Venture

and Owen Tarsley must be prominent.

Tag line should be look cool under the title.

Must be very modern and cool. Needs to catch people's eyes so needs to be really punchy.

Nice to have
• Maybe a clock or stopwatch icon would be cool to add in there so it isn't just plain.. Similar to like how the books have a cool icon with them that I have attached in the uploaded images.
Should not have
• I like simplicity, artistic and very high impact. It really needs to draw you in and catch your eye.

Don't use plain boring fonts. Although I like simplicity slick design is very important - I dont want it to be boring - it has to look high quality and expensive. Therefore do not use fonts like Arial, Times New Roman those really boring fonts that make it look cheap. If I was going to do something like that then I might as well do it myself.

If you want to see the quality of things that I am usually involved with look at the artwork for one of my events that I run called Velvetide: http://www.velvetide.example/velvetide-gala-anthems-ft-korbanhale-autumn-eve-nine-report/

That will give you an idea of what type of quality things that I am involved with, so you need to be up for the task..

```html
<!DOCTYPE html>
<html lang="en">
<head>
<meta charset="utf-8">
<title>The Quick Lane Venture — Book Cover</title>
<link rel="stylesheet" href="https://fonts.googleapis.com/css2?family=Poiret+One&family=Open+Sans:ital,wght@0,400;1,400&display=swap">
<style>
  :root {
    --charcoal: #1b1b1b;
    --charcoal-streak: #222222;
    --spine: #121212;
    --lime: #cbdc26;
    --white: #ffffff;
    --body-text: #ececec;
    --rule: #3a3a3a;
    --photo-light: #9aa3a8;
    --photo-dark: #4a4540;
    --icon-blue: #4fb8d4;
    --icon-lime: #a6d92a;
  }
  * { margin: 0; padding: 0; box-sizing: border-box; }
  html, body {
    width: 1200px;
    height: 834px;
    overflow: hidden;
    background: var(--charcoal);
  }
  .cover {
    position: relative;
    width: 1200px;
    height: 834px;
    background:
      repeating-linear-gradient(90deg, transparent 0 3px, var(--charcoal-streak) 3px 4px, transparent 4px 9px),
      var(--charcoal);
    font-family: "Open Sans", sans-serif;
    color: var(--white);
  }
  .spine {
    position: absolute;
    left: 570px;
    top: 0;
    width: 60px;
    height: 834px;
    background: linear-gradient(90deg, #161616, var(--spine) 40%, var(--spine) 60%, #161616);
  }

  /* Back cover */
  .author-photo {
    position: absolute;
    left: 230px;
    top: 120px;
    width: 117px;
    height: 117px;
    border-radius: 50%;
    background: radial-gradient(circle at 50% 45%, var(--photo-light), var(--photo-dark));
  }
  .back-author-name {
    position: absolute;
    left: 0;
    width: 576px;
    top: 259px;
    text-align: center;
    font-family: "Poiret One", sans-serif;
    font-weight: 400;
    font-size: 20px;
    color: var(--lime);
  }
  .back-blurb {
    position: absolute;
    left: 52px;
    top: 290px;
    width: 467px;
    font-size: 11px;
    line-height: 16px;
    letter-spacing: 1.45px;
    text-align: justify;
    color: var(--body-text);
  }
  .testimonial {
    position: absolute;
    font-style: italic;
    font-size: 13px;
    letter-spacing: 1.6px;
    color: var(--body-text);
  }
  .testimonial--back { left: 46px; top: 420px; }
  .testimonial--front { left: 630px; width: 570px; top: 679px; text-align: center; }
  .price {
    position: absolute;
    left: 74px;
    top: 700px;
    font-family: "Poiret One", sans-serif;
    font-size: 29px;
    color: var(--lime);
  }

  /* Front cover */
  .cover-icon {
    position: absolute;
    left: 878px;
    top: 40px;
    width: 82px;
    height: 86px;
    border-radius: 50%;
    background: radial-gradient(circle at 50% 55%, var(--icon-lime) 0 45%, var(--icon-blue) 75%);
  }
  .title {
    position: absolute;
    left: 630px;
    width: 570px;
    top: 138px;
    text-align: center;
    font-family: "Poiret One", sans-serif;
    font-weight: 400;
    color: var(--white);
    line-height: 1;
  }
  .title-line-top { display: block; font-size: 68px; letter-spacing: 1px; }
  .title-accent { color: var(--lime); }
  .title-line-main { display: block; font-size: 124px; margin-top: -8px; }
  .tagline {
    position: absolute;
    left: 691px;
    width: 453px;
    top: 337px;
    padding: 8px 0;
    border-top: 1px solid var(--rule);
    border-bottom: 1px solid var(--rule);
    text-align: center;
    font-size: 15px;
    letter-spacing: 2.2px;
    color: var(--lime);
    white-space: nowrap;
  }
  .front-author {
    position: absolute;
    left: 693px;
    width: 452px;
    top: 740px;
    display: flex;
    align-items: center;
    gap: 18px;
    font-family: "Poiret One", sans-serif;
    font-size: 46px;
    color: var(--lime);
    white-space: nowrap;
  }
  .front-author::before,
  .front-author::after {
    content: "";
    flex: 1;
    height: 1px;
    background: var(--lime);
  }
</style>
</head>
<body>
<main class="cover">
  <section class="back-cover">
    <div class="author-photo" role="img" aria-label="Portrait photo of the author, Owen Tarsley"></div>
    <h2 class="back-author-name">Owen Tarsley</h2>
    <p class="back-blurb">Lorem Ipsum is simply dummy text of the printing and typesetting industry. Lorem Ipsum has been the industry's standard dummy text ever since the 1500s, when an unknown printer took a galley of type and scrambled it to make a type specimen book. It has survived not only five centuries, but also the leap into electronic typesetting, remaining essentially unchanged.</p>
    <p class="testimonial testimonial--back">“Room for quote/testimonial”</p>
    <p class="price">$19.95</p>
  </section>

  <div class="spine"></div>

  <section class="front-cover">
    <div class="cover-icon" role="img" aria-label="Alarm clock illustration in blue and lime"></div>
    <h1 class="title">
      <span class="title-line-top">The <span class="title-accent">Quick</span> Lane</span>
      <span class="title-line-main">Venture</span>
    </h1>
    <p class="tagline">START AN ONLINE BUSINESS IN NO TIME AT ALL</p>
    <p class="testimonial testimonial--front">“Room for quote/testimonial”</p>
    <p class="front-author">Owen Tarsley</p>
  </section>
</main>
</body>
</html>
```